Pale Thistle Annals Trilogy - new Fantasy book series

Design of front cover and spine for each book in this trilogy based on the images attached.

The titles are as follows:
Book 1 - Heron's Lantern
Book 2 - Embers of Dusk
Book 3 - Stag of Hollowmere

Author - Clive Marlowe (and he is also the illustrator of these cover images)

The book size is b-format (W X H mm: 129 x 198)

Target Market(s)

This is a fantasy series for the age group 14+ and appeals to both male and female readers

Industry/Entity Type

Publishing

Requirements
Must have
• The images supplied are key to this brief as these are by the author.
• These images can be trimmed to suit your designs but the characters must remain the focus and intact.
• Series Title
• Book Title
• No of book in series
• Author's name
• Company logo (Fenwick & Taverley)
• Spine Design with Series name, Book no of Series, Title, Author, Company Logo
Nice to have
• A font that is appropriate to the Fantasy genre.
• The stories are set in Victorian Britain and there is a battle between good and evil. The images supplied for the front covers are of the good characters.
• To see what the Pale Thistle Annals is all about please visit the facebook page: https://www.exampleface.net/palethistleannals/
• Existing book covers are shown on this page both in posts and the fb store.

```html
<!DOCTYPE html>
<html lang="en">
<head>
<meta charset="utf-8">
<title>Embers of Dusk – Pale Thistle Annals Book 2 – Cover Wrap</title>
<link rel="stylesheet" href="https://fonts.googleapis.com/css2?family=Cinzel:wght@400;700;900&family=IM+Fell+English&family=Oswald:wght@600&display=swap">
<style>
  :root {
    --page-bg: #ecebe8;
    --sky-blue: #4fa3d6;
    --deep-blue: #1d2f8c;
    --night: #0b0f2a;
    --gold-light: #ffe27a;
    --gold: #e0a430;
    --gold-dark: #7a3d0c;
    --ink-white: #f4f4f4;
    --blurb-ink: #2a1a0a;
    --blurb-panel: rgba(190, 180, 220, 0.55);
    --wrap-w: 1110px;
    --wrap-h: 760px;
  }
  * { box-sizing: border-box; margin: 0; padding: 0; }
  html, body { width: 1200px; height: 1200px; overflow: hidden; }
  body {
    background: var(--page-bg);
    display: flex;
    align-items: center;
    justify-content: center;
  }
  .cover-wrap {
    width: var(--wrap-w);
    height: var(--wrap-h);
    display: grid;
    grid-template-columns: 500px 110px 500px;
    box-shadow: 0 10px 30px rgba(0,0,0,0.25);
  }
  .title-gold {
    font-family: "Oswald", "Cinzel", sans-serif;
    font-weight: 600;
    text-transform: uppercase;
    letter-spacing: -1px;
    white-space: nowrap;
    background: linear-gradient(180deg, var(--gold-light) 0%, var(--gold) 50%, var(--gold-dark) 100%);
    -webkit-background-clip: text;
    background-clip: text;
    color: transparent;
    filter: drop-shadow(2px 3px 2px rgba(0,0,0,0.6));
  }
  /* Back cover */
  .back-cover {
    position: relative;
    overflow: hidden;
    background: linear-gradient(180deg, var(--sky-blue) 0%, #3d7fc4 35%, var(--deep-blue) 60%, #1a2470 100%);
  }
  .back-cover .art-knight {
    position: absolute;
    left: 20px; bottom: 60px;
    width: 460px; height: 230px;
    border-radius: 40% 50% 30% 40%;
    background: radial-gradient(ellipse at 40% 50%, #c89a4a 0%, #a8402a 45%, rgba(60,30,80,0) 75%);
    opacity: 0.85;
  }
  .back-cover .title-gold {
    position: absolute; top: 125px; left: 0; right: 0;
    text-align: center;
    font-size: 62px;
    line-height: 1;
    transform: scaleY(1.15);
  }
  .blurb {
    position: absolute;
    top: 240px; left: 30px; right: 30px;
    padding: 22px 20px;
    background: var(--blurb-panel);
    font-family: "IM Fell English", serif;
    font-size: 27px;
    line-height: 1.35;
    color: var(--blurb-ink);
    text-align: center;
  }
  .blurb p + p { margin-top: 18px; }
  .imprint {
    font-family: "Cinzel", serif;
    font-weight: 700;
    color: var(--ink-white);
    text-align: center;
    white-space: nowrap;
  }
  .back-cover .imprint { position: absolute; bottom: 70px; left: 0; right: 0; font-size: 20px; }
  .author {
    font-family: "Cinzel", serif;
    color: var(--ink-white);
    letter-spacing: 8px;
    text-transform: uppercase;
    text-align: center;
    white-space: nowrap;
  }
  .back-cover .author { position: absolute; bottom: 28px; left: 0; right: 0; font-size: 24px; }

  /* Spine */
  .spine {
    position: relative;
    overflow: hidden;
    background: linear-gradient(90deg, #1b2460 0%, #2e3a9a 50%, #1b2460 100%);
    display: flex;
    flex-direction: column;
    align-items: center;
    justify-content: space-between;
    padding: 22px 0 16px;
  }
  .spine-vertical {
    writing-mode: vertical-rl;
    white-space: nowrap;
    flex: none;
  }
  .spine .title-gold { font-size: 38px; line-height: 1.1; }
  .spine-series {
    font-family: "Cinzel", serif;
    color: var(--ink-white);
    font-size: 22px;
    line-height: 1.05;
    text-align: start;
  }
  .spine-number {
    font-family: "Cinzel", serif;
    font-weight: 900;
    font-size: 44px;
    line-height: 1;
    color: var(--gold);
  }
  .spine .author { font-size: 15px; letter-spacing: 7px; line-height: 1; }
  .spine .imprint { font-size: 10px; line-height: 1.2; white-space: normal; padding: 0 6px; }

  /* Front cover */
  .front-cover {
    position: relative;
    overflow: hidden;
    background: linear-gradient(160deg, #5aa8d8 0%, #3b78b8 40%, #22308c 70%, #0d1238 100%);
  }
  .front-cover .art-witch {
    position: absolute;
    left: 90px; top: 240px;
    width: 380px; height: 520px;
    border-radius: 45% 45% 20% 30%;
    background: radial-gradient(ellipse at 55% 45%, #8a5a30 0%, #5a3a20 45%, rgba(40,30,20,0) 75%);
  }
  .front-cover .title-gold {
    position: absolute; top: 70px; left: 0; right: 20px;
    text-align: right;
    font-size: 66px;
    line-height: 1;
    transform: scaleY(1.15);
  }
  .front-series {
    position: absolute; top: 168px; right: 30px;
    font-family: "Cinzel", serif;
    color: var(--ink-white);
    font-size: 34px;
    text-align: right;
    line-height: 1.1;
    white-space: nowrap;
  }
  .front-series .book-no { display: block; font-size: 30px; margin-right: 90px; }
  .front-cover .imprint { position: absolute; bottom: 80px; left: 160px; right: 0; font-size: 22px; }
  .front-cover .author { position: absolute; bottom: 34px; left: 120px; right: 0; font-size: 30px; }
</style>
</head>
<body>
  <main class="cover-wrap">
    <section class="back-cover">
      <div class="art-knight" role="img" aria-label="Illustration of an armoured knight in gold and red plate, lying across the lower cover"></div>
      <h2 class="title-gold">Embers of Dusk</h2>
      <div class="blurb">
        <p>The Witches as the are forced into conflict with their old enemy the Knights of the Illuminati.</p>
        <p>It is about to get perilous!</p>
      </div>
      <div class="imprint">Fenwick &amp; Taverley</div>
      <div class="author">Clive Marlowe</div>
    </section>

    <section class="spine">
      <span class="spine-vertical title-gold">Embers of Dusk</span>
      <span class="spine-vertical spine-series">Pale Thistle<br>Annals</span>
      <span class="spine-number">2</span>
      <span class="spine-vertical author">Clive Marlowe</span>
      <div class="imprint">Fenwick &amp; Taverley</div>
    </section>

    <section class="front-cover">
      <div class="art-witch" role="img" aria-label="Illustration of a witch in a brown hat and leather coat kneeling with a staff, a small pale winged creature on her shoulder, in a misty blue landscape"></div>
      <h1 class="title-gold">Embers of Dusk</h1>
      <div class="front-series">Pale Thistle Annals<span class="book-no">Book 2</span></div>
      <div class="imprint">Fenwick &amp; Taverley</div>
      <div class="author">Clive Marlowe</div>
    </section>
  </main>
</body>
</html>
```